Publisher Needs New Book Cover for Popular India Travel Book & New Logo

This is for the second edition of the first book in a series, "Savoring Peru: The Complete Pocket Guide", which has been quite popular. The cover should have a photo.

We intend to hire the winning designer for other projects in the near future, as well.

Current cover is attached. All the text would essentially be the same with the addition of "Second Edition" somewhere.

The logo might be a combination of words and an image, but it should be compact or at least have a compact element that will fit comfortably on the spine of a book. Since this is part of a series (the second book is called "Roam Boldly Through Chile: What Each Lady Must Learn About Staying Secure)

Target Market(s)

Travelers to India

Industry/Entity Type

Travel

Logo Text

Marrowind Books LLC

Requirements
Must have
• Lighter, more uplifting colors are what we like.
• Since this is part of a series (the second book is called "Roam Boldly Through Chile: What Each Lady Must Learn About Staying Secure), there needs to be some unique design element that can be used in the whole Savoring Peru series.
Nice to have
• Tourists in the photo—at least one Caucasian, but it would be good to have other ethnicities as well—looking happy. Women should be fairly modestly dressed.
Should not have
• No black text or other design elements.

```html
<!DOCTYPE html>
<html lang="en">
<head>
<meta charset="utf-8">
<title>Savoring Peru: The Complete Pocket Guide — Second Edition</title>
<link rel="stylesheet" href="https://fonts.googleapis.com/css2?family=Anton&family=Archivo+Black&family=EB+Garamond:ital@1&family=Oswald:wght@600&display=swap">
<style>
  :root {
    --cover-blue: #5a7cff;
    --cover-blue-light: #7d98ff;
    --title-red: #ee2a2a;
    --outline-white: #ffffff;
    --accent-sun: #ffc93c;
    --text-white: #ffffff;
  }
  * { margin: 0; padding: 0; box-sizing: border-box; }
  html, body { width: 799px; height: 1200px; overflow: hidden; }
  body { background: var(--cover-blue); }
  .cover {
    position: relative;
    width: 799px;
    height: 1200px;
    background: linear-gradient(180deg, var(--cover-blue-light) 0%, var(--cover-blue) 100%);
    overflow: hidden;
  }
  .series-mark {
    position: absolute;
    left: 66px;
    top: 190px;
    display: flex;
    align-items: center;
    gap: 10px;
  }
  .series-mark__square {
    width: 18px;
    height: 18px;
    background: var(--accent-sun);
  }
  .series-mark__name {
    font-family: "Oswald", sans-serif;
    font-weight: 600;
    font-size: 28px;
    line-height: 34px;
    color: var(--text-white);
  }
  .title-lockup {
    position: absolute;
    left: 322px;
    top: 60px;
    width: 380px;
  }
  .outlined {
    color: var(--title-red);
    -webkit-text-stroke: 5px var(--outline-white);
    paint-order: stroke fill;
  }
  .title__lead {
    display: block;
    font-family: "Archivo Black", sans-serif;
    font-size: 56px;
    line-height: 62px;
    letter-spacing: -0.5px;
  }
  .title__main {
    display: block;
    font-family: "Anton", sans-serif;
    font-size: 116px;
    line-height: 116px;
    margin-top: -2px;
    letter-spacing: -1px;
  }
  .title__sub {
    display: block;
    font-family: "Archivo Black", sans-serif;
    font-size: 22.5px;
    line-height: 26px;
    margin-top: 4px;
    -webkit-text-stroke: 4px var(--outline-white);
  }
  .endorsement {
    position: absolute;
    left: 318px;
    top: 282px;
    width: 440px;
    font-family: "EB Garamond", serif;
    font-style: italic;
    color: var(--text-white);
  }
  .endorsement__quote { font-size: 31px; line-height: 36px; }
  .endorsement__source {
    font-size: 17px;
    line-height: 20px;
    text-align: right;
    padding-right: 6px;
  }
  .series-band {
    position: absolute;
    left: 0;
    width: 799px;
    height: 8px;
    background: var(--accent-sun);
  }
  .series-band--top { top: 362px; }
  .series-band--bottom { top: 830px; }
  .cover-photo {
    position: absolute;
    left: 0;
    top: 370px;
    width: 799px;
    height: 460px;
    background: linear-gradient(180deg, #e6e8ea 0%, #dad9d2 35%, #c4b3a0 62%, #9a9877 80%, #7c8863 100%);
  }
  .edition {
    position: absolute;
    left: 66px;
    top: 870px;
    font-family: "Archivo Black", sans-serif;
    font-size: 26px;
    line-height: 32px;
    color: var(--text-white);
    letter-spacing: 1px;
    text-transform: uppercase;
  }
  .credit {
    position: absolute;
    left: 508px;
    top: 1050px;
    font-family: "Archivo Black", sans-serif;
    font-size: 31px;
    line-height: 38px;
    -webkit-text-stroke: 4px var(--outline-white);
  }
</style>
</head>
<body>
  <main class="cover">
    <div class="series-mark">
      <span class="series-mark__square"></span>
      <span class="series-mark__name">Wander Peru</span>
    </div>

    <h1 class="title-lockup">
      <span class="title__lead outlined">Savoring</span>
      <span class="title__main outlined">Peru</span>
      <span class="title__sub outlined">The Complete Pocket Guide</span>
    </h1>

    <blockquote class="endorsement">
      <p class="endorsement__quote">“ A must read for all visitors”</p>
      <p class="endorsement__source">Priya Lindqvist, Open Road Tours</p>
    </blockquote>

    <div class="series-band series-band--top"></div>
    <div class="cover-photo" role="img" aria-label="Photo of smiling travellers wearing marigold garlands greeting a local guide with palms pressed together, a white marble monument behind them"></div>
    <div class="series-band series-band--bottom"></div>

    <p class="edition">Second Edition</p>

    <p class="credit outlined">by:<br>M.R. Talvanen</p>
  </main>
</body>
</html>
```